New Web Design Project shop crate

We are about to start a new furniture selling website and it will be based on shop crate . we mainly need two pages designing landing page & item page. so come up with your unique ideas and designs . Please make sure the design needs to be unique . no templates and themes . Will make the selected designer even happier if your design is selected. So basically over all it is going to be the new theme for our shop crate base eCommerce website .we will appreciate if its responsive with some unique features .
SO as per request of designers about more brief about the project = WE ONLY NEED A RESPONSIVE THEME FOR OUR SHOP CRATE BASE eCommerce WebSite . Mainly item page & product page needs a good unique design. Lighter, speed load, compatible with all browsers and responsive will be appreciated . To Get an idea check on sofahaven .co .uk website or chairmeadow etc.
more projects coming soon .

Target Market(s)

Our audience will be furniture buying customers .

Industry/Entity Type

Furniture

Requirements
Must have
• to get some sort of idea have a look at sofahaven .co uk`s website`s listing page and landing page .
Nice to have
• responsive, easy to customize, full theme .

```html
<!DOCTYPE html>
<html lang="en">
<head>
<meta charset="utf-8">
<title>Timber Loft — Furniture Store</title>
<link href="https://fonts.googleapis.com/css2?family=Roboto:wght@300;400&family=Source+Sans+3:wght@400;600&display=swap" rel="stylesheet">
<style>
:root{
  --ink:#333;
  --muted:#9a9a9a;
  --orange:#f7941d;
  --pink:#e8185a;
  --green:#6b9a1e;
  --teal:#1fa7b3;
  --magenta:#ea2a6b;
  --dark:#1c1c1c;
  --footer:#f2f2f2;
  --card:#ececec;
  --wood1:#f8e7b8;
  --wood2:#f2d898;
}
*{box-sizing:border-box;margin:0;padding:0}
html,body{width:854px;height:1200px;overflow:hidden}
body{position:relative;background:#fff;font-family:"Source Sans 3",sans-serif;color:var(--ink)}
a{color:inherit;text-decoration:none}
.abs{position:absolute}

/* header */
.brand{left:83px;top:28px;display:flex;align-items:center;gap:8px}
.brand-mark{width:26px;height:26px;background:var(--pink);border-radius:5px}
.brand-name{font-size:28px;font-weight:400;color:#2a2a2a}
.toplinks{left:477px;top:9px;width:294px;display:flex;justify-content:space-around;font-size:8.5px;color:#777;border-bottom:1px solid #ddd;padding-bottom:9px}
.social{display:flex;gap:4px}
.social span{width:16px;height:16px;border-radius:50%;display:block}
.s1{background:#7ec8e3}.s2{background:#f07c7c}.s3{background:#4a66a8}
.phone{left:582px;top:50px;font-size:11px;display:flex;align-items:center;gap:4px}
.search{left:477px;top:69px;width:192px;height:24px;border:1px solid #ddd;border-radius:2px;font-size:8px;color:#888;padding:7px 9px;background:#fafafa}
.search svg{position:absolute;right:8px;top:5px}
.cart{left:675px;top:44px;width:83px;height:54px;background:var(--orange);color:#fff;padding:10px 10px}
.cart b{font-weight:600;font-size:12px;margin-left:6px}
.cart small{display:block;font-size:7.5px;margin-top:9px;text-align:center}
.nav{left:83px;top:98px;width:688px;height:35px;background:var(--dark);border-radius:4px 4px 0 0;display:flex;justify-content:space-around;align-items:center;color:#fff;font-size:11.5px}

/* hero */
.hero-bg{left:0;top:133px;width:854px;height:439px;background:linear-gradient(90deg,var(--wood2),var(--wood1) 30%,var(--wood2) 60%,var(--wood1))}
.photo{position:absolute}
.slide{left:83px;top:133px;width:439px;height:293px;background:linear-gradient(160deg,#6b5436,#c89a6a 45%,#a25a3a 75%,#4d3a26)}
.caption{left:83px;top:363px;width:439px;height:63px;background:var(--orange);color:#fff;padding:6px 18px}
.caption h2{font-family:Roboto,sans-serif;font-weight:300;font-size:22px;line-height:1.1}
.caption p{font-size:7px;line-height:1.3;margin-top:3px}
.dots{left:460px;top:345px;display:flex;gap:5px}
.dots i{width:9px;height:9px;border-radius:50%;background:#fff;display:block}
.dots i:first-child{background:var(--pink)}
.band{position:absolute;left:522px;width:249px;color:#fff;font-family:Roboto,sans-serif;font-weight:300;font-size:21px;text-align:right;padding:4px 8px}
.cat{position:absolute;top:426px;height:146px;width:146px;display:flex;align-items:center;justify-content:center;color:#fff;font-family:Roboto,sans-serif;font-weight:300;font-size:24px}

/* intro */
.intro-title{left:0;top:598px;width:854px;text-align:center;font-family:Roboto,sans-serif;font-weight:300;color:var(--pink);font-size:23px}
.intro-text{left:92px;top:635px;width:670px;text-align:center;font-size:8.6px;line-height:1.25;color:#555}
.more{left:388px;top:682px;width:79px;height:22px;background:var(--pink);color:#fff;border-radius:3px;font-size:12px;text-align:center;line-height:22px}

/* products */
.card{position:absolute;top:728px;width:157px;height:237px;background:var(--card);border-radius:2px;padding:6px}
.card .img{height:145px}
.price{color:var(--orange);font-weight:600;font-size:11px;margin:5px 0 0 6px}
.pname{font-size:12px;margin-left:6px;color:#444}
.pdesc{font-size:8px;color:var(--muted);margin:3px 6px;line-height:1.3}
.actions{display:flex;gap:6px;margin:5px 0 0 4px;align-items:center}
.add{background:var(--orange);color:#fff;font-size:8px;padding:4px 6px;border-radius:2px}
.icon{width:17px;height:17px;background:#fff;border:1px solid #ccc;border-radius:2px;display:flex;align-items:center;justify-content:center;font-size:8px;color:#666}

/* footer */
.footer{left:0;top:1003px;width:854px;height:197px;background:var(--footer);border-top:2px solid #cfcfcf}
.fcol{position:absolute;top:1030px;width:103px}
.fcol h3{font-weight:400;font-size:13px;padding-bottom:2px;border-bottom:1.5px solid}
.fcol ul{list-style:none;margin-top:10px}
.fcol li{font-size:8px;color:#555;height:21px}
.fcol li::before{content:"➡ ";color:#888;font-size:7px}
.fbrand{left:83px;top:1163px;display:flex;align-items:center;gap:6px;font-size:8px}
.fbrand .brand-mark{width:14px;height:14px;border-radius:3px}
.fbrand b{font-weight:600;font-size:11px}
.fsocial{left:703px;top:1164px}
.fsocial span{width:18px;height:18px}
</style>
</head>
<body>

<header>
  <div class="abs brand"><span class="brand-mark"></span><span class="brand-name">Timber Loft</span></div>
  <nav class="abs toplinks"><a>Home</a><a>Wish List (0)</a><a>My Account</a><a>Shopping Cart</a><a>Checkout</a></nav>
  <div class="abs social" style="left:504px;top:47px"><span class="s1"></span><span class="s2"></span><span class="s3"></span></div>
  <div class="abs phone">
    <svg width="9" height="10" viewBox="0 0 24 24"><path fill="#555" d="M6.6 10.8a15 15 0 0 0 6.6 6.6l2.2-2.2c.3-.3.7-.4 1-.2 1.1.4 2.3.6 3.6.6.6 0 1 .4 1 1V20c0 .6-.4 1-1 1A17 17 0 0 1 3 4c0-.6.4-1 1-1h3.5c.6 0 1 .4 1 1 0 1.3.2 2.5.6 3.6.1.3 0 .7-.2 1z"/></svg>
    0800-555-0199
  </div>
  <div class="abs search">Enter your search
    <svg width="14" height="14" viewBox="0 0 14 14"><circle cx="6" cy="6" r="4.5" fill="none" stroke="#999" stroke-width="1.4"/><path d="M9.5 9.5l3.5 3.5" stroke="#999" stroke-width="1.6"/></svg>
  </div>
  <div class="abs cart">
    <svg width="20" height="15" viewBox="0 0 20 15"><path d="M1 1h3l2 9h10l2-7H5" fill="none" stroke="#fff" stroke-width="2"/><circle cx="8" cy="13" r="1.5" fill="#fff"/><circle cx="15" cy="13" r="1.5" fill="#fff"/></svg><b>Cart</b>
    <small>0 Items - $0.00</small>
  </div>
  <nav class="abs nav"><a>Living Room</a><a>Dining Room</a><a>Bedroom</a><a>Accent Chairs</a><a>Accessories</a><a>Kids' World</a><a>Office</a></nav>
</header>

<section>
  <div class="abs hero-bg" role="img" aria-label="Light pine wood background"></div>
  <div class="photo slide" role="img" aria-label="Ornate cream bedroom with carved bed and peach bedding"></div>
  <div class="abs dots"><i></i><i></i><i></i></div>
  <div class="abs caption">
    <h2>Phasellus blandit velit at fgilla landit velit</h2>
    <p>Mauris orci dolor, sodales quis ante nec, euismod viverra neque. Aeneanquis lorem eget nisl pharetra eleif-<br>end. Praesent ullamcorper odio odio,</p>
  </div>

  <div class="photo" style="left:522px;top:133px;width:249px;height:113px;background:linear-gradient(160deg,#d8d8d6,#9aa4a8 55%,#6f7a80)" role="img" aria-label="Classic blue upholstered sofa"></div>
  <div class="band" style="top:246px;height:32px;background:var(--green)">Modern Sofas</div>
  <div class="photo" style="left:522px;top:278px;width:249px;height:115px;background:linear-gradient(170deg,#e6e6e4,#a8a8a6 60%,#4a4a4a)" role="img" aria-label="Dining room with glass table and cabinets"></div>
  <div class="band" style="top:393px;height:33px;background:var(--teal)">Modern Chairs</div>
  <div class="photo" style="left:522px;top:426px;width:249px;height:112px;background:linear-gradient(170deg,#f0f0f0,#c8c8c8 60%,#6a625a)" role="img" aria-label="White canopy daybed with cushions"></div>
  <div class="band" style="top:538px;height:34px;background:var(--magenta)">New Arrival 2014</div>

  <div class="cat" style="left:83px;background:linear-gradient(160deg,#3a3530,#1e1b18)" role="img" aria-label="Dark showroom with console table">SHOP</div>
  <div class="cat" style="left:229px;background:linear-gradient(160deg,#4a4034,#1f1a15)" role="img" aria-label="Gilded armchair in dark room">DESIGN</div>
  <div class="cat" style="left:376px;width:146px;background:linear-gradient(160deg,#2e2a27,#151312)" role="img" aria-label="Antique furniture display">CONSIGN</div>
</section>

<section>
  <h1 class="abs intro-title">Creative Design &amp; Quality Construction</h1>
  <p class="abs intro-text">Mauris vel orci in tortor convallis blandit. Etiam porta, dui in tempor pellentesque, neque ante varius neque, in condimentum metus neque ut mauris. Mauris dignissim luctus nulla, ac condimentum lectus volutpat et. Ut vel hendrerit lacus. Cras dapibus felis tortor, ut eleifend mi vulputate at. Mauris egestas tellus leo, non iaculis mauris laoreet vel. Suspendisse rutrum pellentesque odio quis commodo. Ut bibendum at tellus nec consectetur.</p>
  <a class="abs more">More</a>
</section>

<section>
  <article class="card" style="left:83px">
    <div class="img" style="background:linear-gradient(160deg,#8a6a3a,#c59a5e 50%,#5a4224)" role="img" aria-label="Gold tufted sofa in a living room"></div>
    <p class="price">$119.50</p><p class="pname">Incididunt ut</p>
    <p class="pdesc">We care about our clients and never let them down. From anci..</p>
    <div class="actions"><span class="add">Add to cart</span><span class="icon">★</span><span class="icon">▣</span></div>
  </article>
  <article class="card" style="left:259px">
    <div class="img" style="background:radial-gradient(circle at 50% 50%,#3a3530,#fff 70%)" role="img" aria-label="Black round pedestal table with gold details"></div>
    <p class="price">$119.50</p><p class="pname">Incididunt ut</p>
    <p class="pdesc">We care about our clients and never let them down. From anci..</p>
    <div class="actions"><span class="add">Add to cart</span><span class="icon">★</span><span class="icon">▣</span></div>
  </article>
  <article class="card" style="left:435px">
    <div class="img" style="background:linear-gradient(170deg,#7a6e62,#e8e0d4 55%,#4a3a2c)" role="img" aria-label="Dining table with cream chairs"></div>
    <p class="price">$119.50</p><p class="pname">Incididunt ut</p>
    <p class="pdesc">We care about our clients and never let them down. From anci..</p>
    <div class="actions"><span class="add">Add to cart</span><span class="icon">★</span><span class="icon">▣</span></div>
  </article>
  <article class="card" style="left:612px">
    <div class="img" style="background:linear-gradient(160deg,#a85a30,#c89a5a 55%,#7a4a28)" role="img" aria-label="Gold clawfoot bathtub with curtains"></div>
    <p class="price">$119.50</p><p class="pname">Incididunt ut</p>
    <p class="pdesc">We care about our clients and never let them down. From anci..</p>
    <div class="actions"><span class="add">Add to cart</span><span class="icon">★</span><span class="icon">▣</span></div>
  </article>
</section>

<footer>
  <div class="abs footer"></div>
  <div class="fcol" style="left:92px"><h3 style="border-color:var(--pink)">Information</h3><ul><li>About Us</li><li>Delivery Information</li><li>Privacy Policy</li><li>Terms &amp; Conditions</li></ul></div>
  <div class="fcol" style="left:280px"><h3 style="border-color:var(--green)">Customer Service</h3><ul><li>Contact Us</li><li>Returns</li><li>Site Map</li></ul></div>
  <div class="fcol" style="left:474px"><h3 style="border-color:var(--orange)">Extras</h3><ul><li>Brands</li><li>Gift Vouchers</li><li>Affiliates</li><li>Specials</li></ul></div>
  <div class="fcol" style="left:668px"><h3 style="border-color:var(--teal)">My Account</h3><ul><li>My Account</li><li>Order History</li><li>Wish List</li><li>Newsletter</li></ul></div>
  <div class="abs fbrand"><span class="brand-mark"></span><b>Timber Loft</b><span>© 2014-Privacy policy</span></div>
  <div class="abs social fsocial"><span class="s1"></span><span class="s2"></span><span class="s3"></span></div>
</footer>

</body>
</html>
```